Grins of Pellbrook - Dental, needs a redesign

Purpose:
Redesign website: http://www.grinsofpellbrook.example/

Sections are important, but for content, we can use existing website or have some placeholder text to fill in later.

Some of the required sections:
About us, contact us, services, our offices, our staff, patient education, patient forms (link to Molavex can be used here), link to friendspace, testimonials

Editability:
We would like to be able to update and edit the content in the future, for small changes

Pictures:
Here is a link to the staff pictures we’d like to use on the website:
https://www.filecrate.example/sh/493kq7zz2tt118p5/BBDRmwLe_uKPi8ZrafQWTGeeb?dl=0
You don't have to use all the pictures; just a few.

friendspace page:
https://www.friendspace.example/Grins-of-Pellbrook-627150384019562

Colors: Calming colors/images for a soothing feeling... to assure the patient that it'll not be that bad.

Target Market(s)

General population

Industry/Entity Type

Dental Clinic

Coding

Coded - Design and coding required

Number of Pages Required

5+ page

Requirements
Must have
• About us, contact us, services, our offices, our staff, patient education, patient forms (link to Molavex can be used here), link to friendspace, testimonials.
• Just create the placeholders for content or use from existing website.
• The staff picture of everyone needs to be on the home page - because that makes it more personal and has received positive feedback from many patients.

```html
<!DOCTYPE html>
<html lang="en">
<head>
<meta charset="utf-8">
<title>Grins of Pellbrook - Dental</title>
<link href="https://fonts.googleapis.com/css2?family=Roboto:ital,wght@0,300;0,400;0,500;0,700;1,400&display=swap" rel="stylesheet">
<style>
:root{
  --purple:#6f4cb3;
  --purple-light:#8a6ad0;
  --teal:#25adb7;
  --teal-dark:#1f9aa3;
  --ink:#3a3a3a;
  --muted:#8a8a8a;
  --footer:#2b2b2b;
  --footer-bar:#1f1f1f;
  --footer-text:#a8a8a8;
  --white:#ffffff;
}
*{margin:0;padding:0;box-sizing:border-box}
html,body{width:1200px;height:2514px;overflow:hidden}
body{position:relative;background:var(--white);font-family:'Roboto',Arial,sans-serif;color:var(--ink)}
.abs{position:absolute}

/* header */
.top-line{left:0;top:0;width:1200px;height:3px;background:var(--purple)}
.brand{left:100px;top:34px;display:flex;align-items:center;gap:12px;white-space:nowrap}
.brand-mark{width:44px;height:44px;border-radius:50%;background:linear-gradient(135deg,var(--purple-light),var(--teal))}
.brand-name{font-size:22px;font-weight:400;color:var(--teal);line-height:1;letter-spacing:1px}
.nav{left:410px;top:51px;display:flex;gap:22px;font-size:11.5px;color:#444;white-space:nowrap}
.nav a{color:inherit;text-decoration:none}
.nav .active{color:var(--purple)}

/* hero */
.hero{left:0;top:117px;width:1200px;height:537px;overflow:hidden}
.hero-photo{position:absolute;inset:0;background:linear-gradient(180deg,#a48b73 0%,#7b6350 35%,#3b3230 70%,#2a2424 100%)}
.hero-waves{position:absolute;left:0;top:0}
.hero-kicker{left:612px;top:303px;font-size:30px;font-weight:700;color:var(--white);white-space:nowrap}
.hero-title{left:610px;top:350px;font-size:54px;font-weight:300;color:var(--purple-light);letter-spacing:1px;white-space:nowrap}
.hero-lead{left:612px;top:430px;width:440px;font-size:19px;font-weight:300;line-height:33px;color:var(--white)}
.hero-btn{left:612px;top:516px;width:204px;height:49px;background:var(--purple);color:var(--white);font-size:14px;display:flex;align-items:center;justify-content:center}
.slider-arrows{left:122px;top:516px;display:flex;gap:2px}
.slider-arrows span{width:24px;height:24px;background:rgba(120,120,120,.8);display:flex;align-items:center;justify-content:center}

/* welcome */
.welcome{left:0;top:654px;width:1200px;height:189px;background:var(--teal);text-align:center;color:var(--white)}
.welcome h1{font-size:25px;font-weight:400;margin-top:32px}
.welcome p{width:970px;margin:18px auto 0;font-size:11.5px;line-height:27px}

/* services */
.service{width:320px;text-align:center;top:891px}
.service-photo{width:312px;height:312px;margin:0 auto;border-radius:50%;box-shadow:0 8px 0 var(--teal),0 13px 0 var(--purple)}
.service h3{margin-top:36px;font-size:15px;font-weight:500;color:var(--teal)}
.service p{margin-top:12px;font-size:12px;line-height:22px;color:var(--muted)}
.dots{left:1070px;top:951px;display:flex;gap:6px}
.dots span{width:13px;height:13px;border-radius:50%;background:#d8d8d8}
.dots span+span{background:#bdbdbd}

/* team */
.team-band{left:0;top:1374px;width:1200px;height:232px;background:linear-gradient(180deg,#3f3633,#2c2624)}
.team-shade{left:0;top:1374px;width:1200px;height:232px;background:rgba(0,0,0,.55)}
.team-head{left:0;top:1410px;width:1200px;text-align:center;color:var(--white)}
.team-head h2{font-size:24px;font-weight:400}
.team-head p{margin-top:10px;font-size:12px;line-height:27px}
.member{width:230px;text-align:center;top:1537px}
.member-photo{width:150px;height:150px;margin:0 auto;border-radius:50%;border:7px solid var(--white);box-shadow:0 0 0 2px var(--teal)}
.member h3{margin-top:16px;font-size:14.5px;font-weight:400;color:var(--purple)}
.member p{width:205px;margin:8px auto 0;font-size:12px;line-height:22px;color:var(--muted)}
.member a{display:block;margin-top:5px;font-size:11.5px;color:var(--purple);text-decoration:none}

/* testimonials */
.rule{left:100px;top:1873px;width:1000px;height:1px;background:#e6e6e6}
.testi-title{left:0;top:1917px;width:1200px;text-align:center;font-size:24px;font-weight:400;color:var(--ink)}
.testi-photo{left:209px;top:1981px;width:128px;height:128px;border-radius:50%;border:5px solid #eee;background:linear-gradient(160deg,#c9a58c,#8a6a58)}
.testi-quote{left:392px;top:1988px;width:600px;font-size:12.5px;font-style:italic;line-height:25px;color:var(--muted)}
.quote-mark{font-size:36px;color:#d5d5d5;font-family:Georgia,serif}
.testi-name{left:392px;top:2081px;font-size:11px;color:var(--purple)}
.testi-role{left:392px;top:2101px;font-size:11.5px;color:var(--muted)}
.testi-arrow{top:2036px;color:#bbb;font-size:22px}

/* footer */
.footer{left:0;top:2157px;width:1200px;height:273px;background:var(--footer)}
.foot-h{font-size:15px;font-weight:400;color:var(--white);top:2194px}
.hours{left:100px;top:2236px;font-size:11.5px;line-height:26px;color:var(--footer-text)}
.contact-row{left:489px;display:flex;gap:14px;font-size:11.5px;line-height:22px;color:var(--footer-text)}
.map{left:751px;top:2199px;width:350px;height:179px;background:linear-gradient(135deg,#e7e3dc,#d7dfd0 55%,#e9e5df)}
.footer-bar{left:0;top:2430px;width:1200px;height:84px;background:var(--footer-bar)}
.bar-links{left:100px;top:2452px;font-size:11px;color:#ddd}
.copy{left:100px;top:2479px;font-size:11px;color:#ddd}
.follow{left:915px;top:2463px;font-size:11px;color:#ddd;display:flex;align-items:center;gap:10px}
.social{width:29px;height:29px;border-radius:50%;background:var(--white);display:flex;align-items:center;justify-content:center}
</style>
</head>
<body>

<div class="abs top-line"></div>
<div class="abs brand">
  <span class="brand-mark"></span>
  <span class="brand-name">Grins of Pellbrook</span>
</div>
<nav class="abs nav">
  <a class="active">Home</a><a>About us</a><a>Services</a><a>Our offices</a><a>Our staff</a><a>Patient education</a><a>Patient forms</a><a>Testimonials</a><a>Contact us</a>
</nav>

<section class="abs hero">
  <div class="hero-photo" role="img" aria-label="Group photo of the dental team seated together in front of a stone fireplace"></div>
  <svg class="hero-waves" width="1200" height="537" viewBox="0 0 1200 537">
    <path d="M0,377 C300,540 800,540 1200,430 L1200,537 L0,537 Z" fill="#6f4cb3"/>
    <path d="M0,437 C400,600 800,560 1200,370 L1200,537 L0,537 Z" fill="#25adb7"/>
  </svg>
</section>
<div class="abs slider-arrows">
  <span><svg width="10" height="10" viewBox="0 0 10 10"><path d="M6.5 1.5 3 5l3.5 3.5" stroke="#fff" stroke-width="1.5" fill="none"/></svg></span>
  <span><svg width="10" height="10" viewBox="0 0 10 10"><path d="M3.5 1.5 7 5 3.5 8.5" stroke="#fff" stroke-width="1.5" fill="none"/></svg></span>
</div>
<div class="abs hero-kicker">GRINS OF PELLBROOK</div>
<div class="abs hero-title">HONESTLY CARING</div>
<p class="abs hero-lead">Welcome to grinsofpellbrook dental surgery &amp; Quality Dentistry...</p>
<div class="abs hero-btn">Click here for more info</div>

<section class="abs welcome">
  <h1>Welcome to Grins of Pellbrook</h1>
  <p>We are committed to excellence in dentistry through up-to-date technology and highly educated professionals.Our doctor and team attend many continuing education classes to increase knowledge and stay on top of the new advances made in the dental field.We alleviate our patients' fears and anxieties by providing a relaxing environment, free of judgment, where patients can feel confident in their care...</p>
</section>

<div class="abs dots"><span></span><span></span></div>
<article class="abs service" style="left:96px">
  <div class="service-photo" role="img" aria-label="Dentist treating a patient in the dental chair" style="background:linear-gradient(150deg,#8fb7c4,#3d5a66 60%,#2a2f36)"></div>
  <h3>Root Canal Treatment</h3>
  <p>Sed ut perspiciatis unde omnis iste natus voluptatem accusantium doloremque laudantium, totam rem aperiam, eaque ipsa quae ab illo...</p>
</article>
<article class="abs service" style="left:440px">
  <div class="service-photo" role="img" aria-label="Dental assistant working with a patient in a treatment room" style="background:linear-gradient(150deg,#b7c7b0,#7e8e80 50%,#5a3c3a)"></div>
  <h3>Extractions</h3>
  <p>Sed ut perspiciatis unde omnis iste natus voluptatem accusantium doloremque laudantium, totam rem aperiam, eaque ipsa quae ab illo...</p>
</article>
<article class="abs service" style="left:784px">
  <div class="service-photo" role="img" aria-label="Four team members posing together in the office" style="background:linear-gradient(150deg,#9a8a78,#5a4a3e 55%,#252222)"></div>
  <h3>Dentures</h3>
  <p>Sed ut perspiciatis unde omnis iste natus voluptatem accusantium doloremque laudantium, totam rem aperiam, eaque ipsa quae ab illo...</p>
</article>

<div class="abs team-band" role="img" aria-label="Faded background photo of the dental team"></div>
<div class="abs team-shade"></div>
<div class="abs team-head">
  <h2>Our Team</h2>
  <p>Nemo enim ipsam voluptatem quia voluptas sit aspernatur aut odit aut fugit, sed quia consequuntur magni dolores eos qui ratione voluptatem sequi nesciunt.<br>Neque porro quisquam est, qui dolorem ipsum quia dolor sit amet, consectetur, adipisci velit, sed quia non numquam</p>
</div>
<article class="abs member" style="left:83px">
  <div class="member-photo" role="img" aria-label="Portrait of the dentist" style="background:linear-gradient(160deg,#b89a86,#4a3a36)"></div>
  <h3>Dr.Meera Kallan</h3>
  <p>Nemo enim ipsam voluptatem quiaers voluptas sit aspernatur aut odit aut fugit, sed quia magni...</p>
  <a>Click read More Information</a>
</article>
<article class="abs member" style="left:351px">
  <div class="member-photo" role="img" aria-label="Portrait of a team member" style="background:linear-gradient(160deg,#c28a6a,#3a3030)"></div>
  <h3>Josie Hartwell</h3>
  <p>Nemo enim ipsam voluptatem quiaers voluptas sit aspernatur aut odit aut fugit, sed quia magni...</p>
  <a>Click read More Information</a>
</article>
<article class="abs member" style="left:619px">
  <div class="member-photo" role="img" aria-label="Portrait of a team member" style="background:linear-gradient(160deg,#b79478,#3a3232)"></div>
  <h3>Renna Collby</h3>
  <p>Nemo enim ipsam voluptatem quiaers voluptas sit aspernatur aut odit aut fugit, sed quia magni...</p>
  <a>Click read More Information</a>
</article>
<article class="abs member" style="left:887px">
  <div class="member-photo" role="img" aria-label="Portrait of a team member" style="background:linear-gradient(160deg,#c4826a,#3a2e2e)"></div>
  <h3>tara Velmont</h3>
  <p>Nemo enim ipsam voluptatem quiaers voluptas sit aspernatur aut odit aut fugit, sed quia magni...</p>
  <a>Click read More Information</a>
</article>

<div class="abs rule"></div>
<h2 class="abs testi-title">Client Testimonials</h2>
<div class="abs testi-arrow" style="left:98px">&#8249;</div>
<div class="abs testi-arrow" style="left:1092px">&#8250;</div>
<div class="abs testi-photo" role="img" aria-label="Portrait of a smiling client"></div>
<span class="abs quote-mark" style="left:366px;top:1975px">&ldquo;</span>
<p class="abs testi-quote">Lorem Ipsum is simply dummy text of the printing and typesetting industry. Lorem Ipsum has been the industry's standard dummy text ever since the 1500s, when an unknown printer took a galley of type and scrambled it to make a type specimen numquam eius modi tempora book...</p>
<span class="abs quote-mark" style="left:720px;top:2050px">&rdquo;</span>
<div class="abs testi-name">MARCUS DELLEN</div>
<div class="abs testi-role">Our Client</div>

<footer class="abs footer"></footer>
<h4 class="abs foot-h" style="left:100px">Clinic Timinigs</h4>
<div class="abs hours">
  Monday: 12:00pm to 6:00pm<br>
  Tuesday: 10:00am to 7:00pm<br>
  Wednesday: Closed<br>
  Thursday: 8:00am to 6:00pm<br>
  Friday: 8:00am to 5:00pm<br>
  Saturday when open: 8:00am to 3:00pm OR 8:00am to 12:00pm
</div>
<h4 class="abs foot-h" style="left:489px">Contact info</h4>
<div class="abs contact-row" style="top:2234px">
  <svg width="12" height="18" viewBox="0 0 12 18"><path d="M6 0a6 6 0 0 0-6 6c0 4.5 6 12 6 12s6-7.5 6-12a6 6 0 0 0-6-6zm0 8.5A2.5 2.5 0 1 1 6 3.5a2.5 2.5 0 0 1 0 5z" fill="#a8a8a8"/></svg>
  <span>418 E. Harlow Street, Suite 2C<br>Pellbrook, IL 61999</span>
</div>
<div class="abs contact-row" style="top:2300px">
  <svg width="14" height="16" viewBox="0 0 14 16"><path d="M3 0 5.5 4 4 6c1 2.2 2.3 3.6 4 4.5l2-1.5 4 2.5-1.3 3C7 15 .5 8 1 1.3z" fill="#a8a8a8"/></svg>
  <span>Call us at: 555-014-2236/2238</span>
</div>
<div class="abs contact-row" style="top:2338px">
  <svg width="16" height="12" viewBox="0 0 16 12"><rect width="16" height="12" rx="1" fill="#a8a8a8"/><path d="M1 1.5 8 7l7-5.5" stroke="#2b2b2b" stroke-width="1.4" fill="none"/></svg>
  <span>info@grinsofpellbrook.example</span>
</div>
<div class="abs map" role="img" aria-label="Street map showing the clinic location with a red pin"></div>

<div class="abs footer-bar"></div>
<div class="abs bar-links">Home &nbsp;/&nbsp; About us &nbsp;/&nbsp; Services &nbsp;/&nbsp; our offices &nbsp;/&nbsp; our staff &nbsp;/&nbsp; Patient education &nbsp;/&nbsp; Patient forms &nbsp;/&nbsp; Testimonials &nbsp;/&nbsp; contact us.</div>
<div class="abs copy">Copyrights©grinsofpellbrook.2016 | Allrights Reserved.</div>
<div class="abs follow">
  <span>Follow With Us :</span>
  <span class="social"></span>
  <span class="social"></span>
  <span class="social"><svg width="14" height="10" viewBox="0 0 14 10"><rect width="14" height="10" rx="1" fill="#1f1f1f"/><path d="M1 1 7 5.5 13 1" stroke="#fff" stroke-width="1.2" fill="none"/></svg></span>
</div>

</body>
</html>
```